General Store Business Card Design

This is a general store with a post office, that sells groceries, papers, and has a café. It is in rural NSW. I would like to see very cheerful designs that have a cupcake and a cup of coffee as the main logo. This must have colours that will look good on a black background for future shirts for the business. For example, maybe a cupcake with pink frosting and a coffee cup that is a bright colour too. Would like the actual logo to be Millbrook Crossing General Store & Café wrapped around the logo picture. Would like for the background of the business card to also be colourful, ie: sprinkles, confetti, etc., with some sort of actual colour as a background as well.

Industry/Entity Type

Store

Contact Information for Business Card

Millbrook Crossing General Store & Café
418 Tulloch Rd.
Millbrook Crossing, NSW, 2343
Phone: 02 6851 9204
Fax: 02 6851 ????
Website: www.??pendingsite.example

Logo Text

Millbrook Crossing General Store & Cafe

```html
<!DOCTYPE html>
<html lang="en">
<head>
<meta charset="utf-8">
<title>Millbrook Crossing General Store &amp; Café – Business Card</title>
<link rel="stylesheet" href="https://fonts.googleapis.com/css2?family=Fredoka:wght@500;600&display=swap">
<style>
  :root {
    --page-bg: #e9e6e2;
    --sky: #8fd0e2;
    --sky-mid: #bfe6f0;
    --sky-light: #e8f7fb;
    --candy: #f2508f;
    --blush: #fbd3e3;
    --seal-ring: #f7b8d2;
    --white: #ffffff;
    --card-shadow: rgba(60, 40, 30, 0.25);
  }
  * { box-sizing: border-box; margin: 0; padding: 0; }
  html, body {
    width: 1200px; height: 900px; overflow: hidden;
    background: var(--page-bg);
    font-family: "Fredoka", sans-serif;
  }
  .sheet {
    width: 1200px; height: 900px;
    display: flex; flex-direction: column;
    align-items: center; justify-content: center; gap: 44px;
  }
  .card {
    position: relative;
    width: 640px; height: 366px;
    border-radius: 4px;
    overflow: hidden;
    background: radial-gradient(ellipse at 50% 45%, var(--sky-light) 0%, var(--sky-mid) 45%, var(--sky) 100%);
    box-shadow: 0 12px 28px var(--card-shadow);
  }

  /* shared seal */
  .seal {
    position: absolute; left: 50%;
    border-radius: 50%;
    transform: translate(-50%, -50%);
    background: var(--blush);
    border: 6px solid var(--seal-ring);
    display: flex; align-items: center; justify-content: center;
    text-align: center;
    z-index: 2;
  }
  .brand-name {
    color: var(--candy);
    font-weight: 600;
    line-height: 1.15;
  }

  /* front */
  .front .stripe-band {
    position: absolute; left: -40px; right: -40px; top: 50%; bottom: -80px;
    transform: rotate(-6deg);
    transform-origin: 50% 0;
    border-top: 8px solid var(--white);
    box-shadow: 0 -14px 0 0 var(--sky-light);
    background: repeating-linear-gradient(115deg,
      var(--candy) 0 18px, var(--white) 18px 30px);
  }
  .front .seal { top: 46%; width: 224px; height: 224px; }
  .front .brand-name { font-size: 23px; padding: 0 18px; }

  /* back */
  .back .info-band {
    position: absolute; left: 0; right: 0; top: calc(50% - 34px); height: 68px;
    background: var(--candy);
    border-top: 5px solid var(--white);
    border-bottom: 5px solid var(--white);
    box-shadow: 0 -10px 0 -2px var(--candy), 0 10px 0 -2px var(--candy);
  }
  .back .contact {
    position: absolute; top: calc(50% - 22px);
    color: var(--white);
    font-weight: 500; font-size: 15px; line-height: 1.35;
    white-space: nowrap;
  }
  .back .address { left: 14px; width: 214px; text-align: right; }
  .back .phones { right: 22px; }
  .back .seal { top: 50%; width: 164px; height: 164px; border-width: 5px; }
  .back .brand-name { font-size: 17px; padding: 0 12px; }
</style>
</head>
<body>
<main class="sheet">

  <section class="card front">
    <div class="stripe-band"></div>
    <div class="seal">
      <p class="brand-name">Millbrook Crossing General Store &amp;&nbsp;Café</p>
    </div>
  </section>

  <section class="card back">
    <div class="info-band"></div>
    <p class="contact address">418 Tulloch Rd. Millbrook<br>Crossing NSW, 2343</p>
    <p class="contact phones">Phone: 02 6851 9204<br>Fax: 02 6851 ????</p>
    <div class="seal">
      <p class="brand-name">Millbrook Crossing General Store &amp;&nbsp;Café</p>
    </div>
  </section>

</main>
</body>
</html>
```